Visitenkarten/Briefpaier/Kassenkassenbelege für Juwelier
Zielgruppe
Mittelständischer Juwelier mit zwei Filialen. Klassischer Schmuck, Uhren und Modeschmuck
Aufgabenstellung
Es müssen für zwei Geschäfte Visitenkarten, Briefpapier (A4) und Kassenkassenbelege (A6) erstellt werden. Logo und fenwiro im Anhang. Ein Farbkonzept besteht noch nicht. Die Idee geht in Richtung Bordeaux-Rot.
Generell:
(1) Sieht erstmal nach viel Beschreibung aus, bitte nicht entmutigen lassen, sind zu 90% nur austauschbare Inhalts-/Kontaktdaten.
(2) Für meine Zwecke reicht es vollkommen aus, wenn bei den Vorschlägen zur Arbeitsersparnis erstmal nur mit einer Adresse gearbeitet wird. Wenn ich dann den zutreffenden Designvorschlag gefunden habe, können wir die zweite Adresse in dem ersten Format umsetzen. Ich denke das spart Zeit und Nerven.
(3) Bitte Angaben wie "Tel.:" oder "USt.- ID:" nicht wörtlich nehmen, es soll dabei klar sein worum es geht; wenn "Telefon" ausgeschrieben besser aussieht, bitte in der optisch ansprechenderen Form verwenden.
(4) Bei Fragen, bitte fragen!
(5) Viel Spass bei dem Projekt - Ich freu' mich auf die Vorschläge!
Visitenkarten(1):
Juwelier Brandauer GmbH
www.juwelier-brandauer-example.de
Visitenkarten(2):
Visitenkarten(generell):
(1) Die einzelnen Daten können durch Hervorhebungen wie Adresse, Kontakt, Online/Internet unterteilt bzw. hervorgehoben werden.
(2) Die Visitenkarten sollen farbig gedruckt werden; geplant ist weiß als Hintergrund ist aber nicht zwingend bei einer guten anderen Idee
Briefpapier:
(1)Absender im Adressfeld für DIN-lang Briefumschläge mit Fenster:
(2)Informationen im Footer/Seitenbereich:
Juwelier Brandauer Gmb..

```html
<!DOCTYPE html>
<html lang="de">
<head>
<meta charset="utf-8">
<title>Juwelier Brandauer – Geschäftsausstattung</title>
<link href="https://fonts.googleapis.com/css2?family=Source+Sans+3:wght@300;400;600&display=swap" rel="stylesheet">
<style>
:root{
  --stage:#636872;
  --paper:#ffffff;
  --tint:#ede8ec;
  --stripe:#e4dfe3;
  --brand:#4a2140;
  --ink:#4b4f57;
  --muted:#7b8088;
  --rule:#e6e4e6;
}
*{margin:0;padding:0;box-sizing:border-box}
html,body{width:1200px;height:1135px;overflow:hidden}
body{background:var(--stage);position:relative;font-family:"Source Sans 3",sans-serif;color:var(--ink)}
address{font-style:normal}
.sheet{position:absolute;background:var(--paper);overflow:hidden}
.band{position:absolute;left:0;right:0;background:var(--tint)}
.band::after{content:"";position:absolute;left:0;right:0;bottom:-6px;height:3px;background:var(--stripe)}
.brand-name{position:absolute;color:var(--brand);font-weight:600;white-space:nowrap;line-height:1}
.contact{position:absolute;color:var(--muted);line-height:1.35;font-weight:400;white-space:nowrap}
.contact strong{color:var(--brand);font-weight:600;text-transform:uppercase;letter-spacing:.03em}
.gap{display:block;height:.45em}

/* Briefbogen */
.letter{left:65px;top:86px;width:681px;height:963px}
.letter .band{top:0;height:135px}
.letter .brand-name{left:74px;top:52px;font-size:30px}
.letter .contact{left:506px;top:29px;font-size:9px;line-height:12.6px}
.sender{position:absolute;left:74px;top:161px;font-size:6px;color:var(--muted);white-space:nowrap}
.sender strong{color:var(--brand);font-weight:600;text-transform:uppercase}
.recipient{position:absolute;left:74px;top:195px;font-size:11px;line-height:16px;font-weight:300}
.fold{position:absolute;left:2px;width:20px;height:1px;background:#aaa}
.subject{position:absolute;left:74px;top:349px;font-size:15px;font-weight:300}
.date{position:absolute;left:480px;top:353px;font-size:10.5px;font-weight:300}
.body-text{position:absolute;left:74px;top:401px;width:525px;font-size:11px;line-height:16px;font-weight:300}
.body-text p+p{margin-top:16px}
.closing{position:absolute;left:74px;top:706px;font-size:11px;font-weight:300}
.legal{position:absolute;top:913px;font-size:8.4px;line-height:12.6px;color:var(--muted);white-space:nowrap}
.letter .foot{position:absolute;left:0;right:0;bottom:0;height:14px;background:var(--tint)}
.letter .foot::before{content:"";position:absolute;left:0;right:0;top:-5px;height:2px;background:var(--stripe)}

/* Kassenbeleg */
.receipt{left:786px;top:86px;width:341px;height:480px}
.receipt .band{top:0;height:105px}
.receipt .brand-name{left:16px;top:30px;font-size:17px}
.receipt .contact{left:223px;top:14px;font-size:7px;line-height:9.2px}
.ruled{position:absolute;left:16px;width:308px;height:1px;background:var(--rule)}
.receipt-note{position:absolute;right:15px;top:447px;text-align:right;font-size:7.4px;line-height:10.5px;letter-spacing:.04em;color:var(--muted)}
.receipt .foot{position:absolute;left:0;right:0;bottom:0;height:7px;background:var(--stripe)}

/* Visitenkarte */
.card{left:786px;top:621px;width:276px;height:175px}
.card .band{top:0;height:83px}
.card .brand-name{left:16px;top:30px;font-size:22px}
.card .contact{top:109px;font-size:7.8px;line-height:12.7px}
.card .foot{position:absolute;left:0;right:0;bottom:6px;height:2px;background:var(--stripe)}
</style>
</head>
<body>

<section class="sheet letter" aria-label="Briefbogen A4">
  <header class="band">
    <span class="brand-name">Juwelier Brandauer</span>
    <address class="contact">
      <strong>Juwelier Brandauer GmbH</strong><br>
      Kornblumenweg 12<br>45100 Beispielstadt<span class="gap"></span>
      Tel.: 0123 456780<br>Fax: 0123 456781<span class="gap"></span>
      info@juwelier-brandauer-example.de<br>www.juwelier-brandauer-example.de
    </address>
  </header>
  <p class="sender"><strong>Juwelier Brandauer GmbH</strong> | Kornblumenweg 12 | 45100 Beispielstadt</p>
  <p class="recipient">Herrn<br>Max Mustermann<br>Musterstraße 00<br>01234 Musterstadt</p>
  <span class="fold" style="top:341px"></span>
  <span class="fold" style="top:482px"></span>
  <span class="fold" style="top:681px"></span>
  <h1 class="subject">Dies ist eine Betreffzeile</h1>
  <p class="date">Datum: 03.05.2014</p>
  <div class="body-text">
    <p>Sehr geehrter Herr Mustermann, jeder Setzer hat für diesen Zweck immer etwas Blindtext parat. Blindtext ist im Umfang von einigen tausend Anschlägen, der für die »äußerliche« Gestaltung einer Publikation verwendet und dessen Inhalt unwichtig ist. Man setzt ihn oft zum Beispiel in verschiedenen Schriften und Schriftgrößen, um anderen zu zeigen, wie eine bestimmte Schrift wirkt.</p>
    <p>Oder man montiert auch komplette ganze Seiten mit sinnlosen Streifen von Blindtext, um das spätere Aussehen der Seiten zu simulieren. Blindtext wird allerdings oft nur für die Teile einer Seite verwendet, die in so kleiner Schrift gesetzt werden, dass sie beim »Überfliegen« ungelesen bleiben.</p>
    <p>Jeder Setzer hat für diesen Zweck immer etwas Blindtext parat. Blindtext ist Umfang von einigen tausend Anschlägen, der für die »äußerliche« Gestaltung einer Publikation verwendet und dessen Inhalt unwichtig ist.</p>
  </div>
  <p class="closing">Mit freundlichen Grüßen</p>
  <p class="legal" style="left:74px">Amtsgericht Beispielstadt HRB 00000<br>Geschäftsführer: Marianne Brandauer</p>
  <p class="legal" style="left:240px">Steuernummer: 000/0000/0000<br>USt.- ID: DE 000111222</p>
  <p class="legal" style="left:387px">Bankverbindung:<br>Beispielbank AG</p>
  <p class="legal" style="left:506px">IBAN: DE00 0000 0000 0000 0000 00<br>BIC: BSPL DE XX</p>
  <div class="foot"></div>
</section>

<section class="sheet receipt" aria-label="Kassenbeleg A6">
  <header class="band">
    <span class="brand-name">Juwelier Brandauer</span>
    <address class="contact">
      <strong>Juwelier Brandauer GmbH</strong><br>
      Kornblumenweg 12<br>45100 Beispielstadt<span class="gap"></span>
      Tel.: 0123 456780<br>Fax: 0123 456781<span class="gap"></span>
      info@juwelier-brandauer-example.de<br>www.juwelier-brandauer-example.de<span class="gap"></span>
      USt.- ID: DE 000111222
    </address>
  </header>
  <span class="ruled" style="top:160px"></span>
  <span class="ruled" style="top:198px"></span>
  <span class="ruled" style="top:236px"></span>
  <span class="ruled" style="top:274px"></span>
  <span class="ruled" style="top:312px"></span>
  <span class="ruled" style="top:350px"></span>
  <span class="ruled" style="top:388px"></span>
  <span class="ruled" style="top:426px"></span>
  <p class="receipt-note">Bei Umtausch oder Reklamation bitte Beleg vorlegen.<br>Barauszahlung ganz oder teilweise ausgeschlossen.</p>
  <div class="foot"></div>
</section>

<section class="sheet card" aria-label="Visitenkarte">
  <header class="band">
    <span class="brand-name">Juwelier Brandauer</span>
  </header>
  <address class="contact" style="left:14px">
    <strong>Juwelier Brandauer GmbH</strong><br>Kornblumenweg 12<br>45100 Beispielstadt
  </address>
  <address class="contact" style="left:138px">
    Tel.: 0123 456780<br>Fax: 0123 456781<br>info@juwelier-brandauer-example.de<br>www.juwelier-brandauer-example.de
  </address>
  <div class="foot"></div>
</section>

</body>
</html>
```